Private Visitenkarte für Naturwissenschaftler
Vielen Dank für die überaus gute und überzeugende Arbeit. Ohne Einschränkung weiterzuempfehlen!
Zielgruppe
Die Zielgruppe sind primär potentielle Arbeitgeber. Diese sind vor allem in der Forschung und Entwicklung im naturwissenschaftlich-technischem Bereich angesiedelt.
Aufgabenstellung
Vorraussetzungen:
1. Die Karte ist zweiseitig bedruckt
2. Auf der Vorderseite steht der Spruch:
"Wenn es schon einem gelungen ist,
so ist es keine Schwierigkeit.
Wenn es noch keinem gelungen ist,
so wird es dafür langsam Zeit!"
3. Auf der Rückseite stehen die Kontaktdaten
4. Auf beiden Seiten ist ein Hintergrund zu sehen.
Die Datei nsg.pdf beinhaltet die sogenannten Navier-Stokesschen Gleichungen. Diese beschreiben Flüssigkeitsströmungen. Der Hintergrund sollte so aufgebaut sein, dass er zum einen diese Gleichungen enthält (exakt wie dargestellt) und zum anderen etwas, dass durch die Gleichungen beschrieben wird, z.B. ein Wasserfall oder der Fluss durch ein Rohr oder auch gerne etwas Abstraktes.
Die Gestaltung also hauptsächlich den Hintergund, sowie Form, Farbe und Ausrichtung des Textes.
Da sich Rufnummern oder E-Mails immer mal ändern, benötige ich am Ende außerdem ein Dateiformat, das das Editieren der Texte erlaubt (am besten als photoshop document).
Anm.: In der Formel ist ein kleiner Fehler, in der zweiten Zeile muss das "u" ein "v" sein

```html
<!DOCTYPE html>
<html lang="de">
<head>
<meta charset="utf-8">
<title>Visitenkarte – Vorder- und Rückseite</title>
<link rel="stylesheet" href="https://fonts.googleapis.com/css2?family=Roboto+Condensed:wght@500&family=Tinos:ital@0;1&display=swap">
<style>
  :root {
    --page: #ffffff;
    --sky-deep: #34507a;
    --sky-mid: #6f8db7;
    --sky-light: #dfe7f2;
    --water-light: #f3f6f8;
    --water-teal: #5aa58f;
    --waterline: #1b2c3f;
    --ink-white: #ffffff;
    --formula-ink: #1f3553;
    --icon-ink: #3a5680;
  }
  * { box-sizing: border-box; margin: 0; padding: 0; }
  html, body { width: 1200px; height: 886px; overflow: hidden; background: var(--page); }
  .sheet { position: relative; width: 1200px; height: 886px; }

  .card {
    position: absolute;
    width: 604px; height: 404px;
    overflow: hidden;
    box-shadow: 8px 14px 28px rgba(0,0,0,.22);
  }
  .card--front { left: 0; top: 2px; }
  .card--back { left: 565px; top: 453px; }

  .card__photo {
    position: absolute; inset: 0;
    background:
      radial-gradient(ellipse 55% 60% at 58% 68%, rgba(255,255,255,.85), rgba(255,255,255,0) 70%),
      linear-gradient(160deg, var(--sky-deep) 0%, var(--sky-mid) 45%, var(--sky-light) 75%);
  }
  .card__photo::after {
    content: ""; position: absolute; left: 0; right: 0; top: 67%; bottom: 0;
    background: linear-gradient(90deg, #c9d5e6 0%, var(--water-light) 30%, #e6f0ec 50%, var(--water-teal) 85%);
    border-top: 2px solid var(--waterline);
  }

  .quote {
    position: absolute; right: 290px; top: 36px;
    font-family: "Roboto Condensed", sans-serif; font-weight: 500;
    font-size: 20px; line-height: 27.5px;
    color: var(--ink-white); text-align: right; white-space: nowrap;
  }
  .quote p + p { margin-top: 5px; }

  .contact {
    position: absolute; left: 47px; top: 32px;
    font-family: "Roboto Condensed", sans-serif; font-weight: 500;
    color: var(--ink-white); white-space: nowrap;
  }
  .contact__name, .contact__title { font-size: 20px; line-height: 27px; }
  .contact__list { list-style: none; margin-top: 10px; }
  .contact__item { display: flex; align-items: center; gap: 7px; font-size: 20px; line-height: 25.5px; margin-left: -3px; }
  .contact__icon { width: 20px; height: 20px; flex: none; }

  .formula {
    position: absolute; right: 22px; bottom: 20px;
    font-family: "Tinos", serif; font-size: 21px; color: var(--formula-ink);
    text-align: center; white-space: nowrap;
  }
  .formula__row { display: flex; align-items: center; gap: 4px; }
  .formula__frac { display: inline-flex; flex-direction: column; align-items: center; line-height: 19px; }
  .formula__frac span:first-child { border-bottom: 1px solid var(--formula-ink); padding: 0 1px; }
  .formula i { font-style: italic; }
  .formula__row--second { justify-content: center; margin-top: 0; padding-left: 18px; }
</style>
</head>
<body>
<main class="sheet">

  <section class="card card--front" aria-label="Vorderseite">
    <div class="card__photo" role="img" aria-label="Foto: Wasserstrahl, der in eine Wasseroberfläche eintaucht, mit Luftblasen unter Wasser"></div>
    <blockquote class="quote">
      <p>„Wenn es schon einem gelungen ist,<br>so ist es keine Schwierigkeit.</p>
      <p>Wenn es noch keinem gelungen ist,<br>so wird es dafür langsam Zeit!“</p>
    </blockquote>
    <div class="formula" aria-label="Navier-Stokes-Gleichungen">
      <div class="formula__row">
        <span class="formula__frac"><span>∂v</span><span><i>∂t</i></span></span>
        <span>+ (v·∇)v = <i>ν</i>∆v − ∇<i>p</i> + f</span>
      </div>
      <div class="formula__row formula__row--second">∇·u = 0</div>
    </div>
  </section>

  <section class="card card--back" aria-label="Rückseite">
    <div class="card__photo" role="img" aria-label="Foto: Wasserstrahl, der in eine Wasseroberfläche eintaucht, mit Luftblasen unter Wasser"></div>
    <div class="contact">
      <p class="contact__name">Tobias Kolbe</p>
      <p class="contact__title">Dipl.-Math. | Dipl.-Phys.</p>
      <ul class="contact__list">
        <li class="contact__item">
          <svg class="contact__icon" viewBox="0 0 20 20" aria-hidden="true"><circle cx="10" cy="10" r="10" fill="#fff"/><path d="M6.5 5.5c.8-.6 1.5-.4 1.9.3l.8 1.5c.3.6.1 1.1-.4 1.5l-.5.4c.5 1.1 1.3 2 2.4 2.5l.5-.5c.4-.5 1-.6 1.5-.3l1.4.8c.7.4.8 1.2.2 1.9-.8.9-2 1.1-3.2.5-2.3-1.2-3.900-2.9-4.900-5.1-.5-1.3-.1-2.6 .3-3.5z" fill="var(--icon-ink)"/></svg>
          <span>04521 738290</span>
        </li>
        <li class="contact__item">
          <svg class="contact__icon" viewBox="0 0 20 20" aria-hidden="true"><circle cx="10" cy="10" r="10" fill="#fff"/><rect x="6.5" y="4" width="7" height="12" rx="1.5" fill="var(--icon-ink)"/><rect x="7.7" y="5.5" width="4.6" height="8" fill="#fff"/></svg>
          <span>0171 5538204</span>
        </li>
        <li class="contact__item">
          <svg class="contact__icon" viewBox="0 0 20 20" aria-hidden="true"><circle cx="10" cy="10" r="10" fill="#fff"/><text x="10" y="14.5" text-anchor="middle" font-family="Roboto Condensed, sans-serif" font-size="15" fill="var(--icon-ink)">@</text></svg>
          <span>tobias.kolbe@verplux.de</span>
        </li>
      </ul>
    </div>
    <div class="formula" aria-label="Navier-Stokes-Gleichungen">
      <div class="formula__row">
        <span class="formula__frac"><span>∂v</span><span><i>∂t</i></span></span>
        <span>+ (v·∇)v = <i>ν</i>∆v − ∇<i>p</i> + f</span>
      </div>
      <div class="formula__row formula__row--second">∇·u = 0</div>
    </div>
  </section>

</main>
</body>
</html>
```